Flyer für Computer Service
Zielgruppe
Privathaushalte und kleinere Firmen.
Wir möchten damit neue Kunden für unsere Dienstleistungen gewinnen.
Aufgabenstellung
Wir möchten mit diesem Flyer speziell unsere Computer Service Dienstleistungen bewerben.
Im wesentlichen werden folgende 3 Kategorieren von Dienstleistungen angeboten:
- Fernwartung
- Reparaturen
- Neuinstallationen, Backups und Virenentfernung
Fernwartung und Reparaturen bieten wir zu "ab EUR xx.-" Preisen an und Neuinstallationen, Backups und Virenentfernung zu Pauschalen.

```html
<!DOCTYPE html>
<html lang="de">
<head>
<meta charset="utf-8">
<title>Pelmaro – Computer Service</title>
<link rel="stylesheet" href="https://fonts.googleapis.com/css2?family=Nunito:wght@700;800;900&display=swap">
<style>
:root{
  --orange:#f07d00;
  --white:#ffffff;
  --ink:#3a3a3a;
  --band-dark:#3c3c3c;
  --footer:#0e0e0e;
  --mid-top:#f2f2f2;
  --mid-bottom:#2a2a2a;
  --placeholder-light:#d9d9d9;
  --placeholder-dark:#bcbcbc;
}
*{margin:0;padding:0;box-sizing:border-box}
html,body{width:849px;height:1200px;overflow:hidden;background:#fff}
.flyer{position:relative;width:849px;height:1200px;overflow:hidden;font-family:"Nunito",Arial,sans-serif;font-weight:800}

/* header */
.header{position:absolute;left:0;top:0;width:849px;height:240px;background:var(--orange)}
.header-photo{position:absolute;left:22px;top:15px;width:270px;height:210px;border:5px solid var(--white);
  background:linear-gradient(135deg,#f4f4f4 0%,#d8d8d8 55%,#bdbdbd 100%)}
.headline{position:absolute;left:322px;top:20px;color:var(--white);font-size:46px;font-weight:900;letter-spacing:1px;
  text-shadow:2px 2px 3px rgba(0,0,0,.45)}
.question{position:absolute;left:322px;top:80px;color:var(--ink);font-size:20px;line-height:26px}
.answer{position:absolute;right:30px;top:140px;width:520px;color:var(--white);font-size:22px;line-height:40px;text-align:right;
  text-shadow:2px 2px 3px rgba(0,0,0,.5)}
.divider-dark{position:absolute;left:0;top:240px;width:849px;height:22px;background:var(--band-dark)}

/* main */
.main{position:absolute;left:0;top:262px;width:849px;height:710px;
  background:linear-gradient(180deg,var(--mid-top) 0%,#d6d6d6 38%,#6e6e6e 56%,var(--mid-bottom) 100%)}
.hand-photo{position:absolute;left:12px;top:40px;width:210px;height:128px;border-radius:6px;
  background:linear-gradient(180deg,var(--placeholder-light),var(--placeholder-dark))}
.laptop-photo{position:absolute;left:37px;top:233px;width:210px;height:160px;border-radius:4px;
  background:linear-gradient(160deg,#2a2a2a,#1f5f8a 45%,#111)}
.pc-photo{position:absolute;left:562px;top:316px;width:218px;height:262px;border-radius:4px;
  background:linear-gradient(90deg,#1a1a1a,#5a5a5a 60%,#9a9a9a)}

.services{position:absolute;left:258px;top:38px;list-style:none;width:500px}
.services li{position:relative;height:50px;display:flex;align-items:center;font-size:28px}
.services li::before{content:"";width:14px;height:14px;background:var(--orange);margin-right:16px}
.service-name{color:#555;text-shadow:1px 1px 0 #fff}
.service-price{position:absolute;right:0;color:#6a6a6a;text-shadow:1px 1px 0 #fff}
.service-price b{color:var(--orange);font-size:34px;font-weight:900;text-shadow:1px 1px 2px rgba(0,0,0,.35)}

.pitch{position:absolute;left:72px;top:430px;color:#e6e6e6;font-size:28px;line-height:50px}
.pitch em{font-style:normal;color:var(--orange)}
.pitch strong{color:var(--orange);font-size:36px;font-weight:900}
.call{position:absolute;left:70px;top:620px;font-size:40px;color:#bdbdbd;font-weight:900;letter-spacing:2px;white-space:nowrap}
.call .phone{color:var(--orange);margin-left:34px;letter-spacing:1px;text-shadow:0 0 3px #fff,1px 1px 0 #fff}

.divider-light{position:absolute;left:0;top:972px;width:849px;height:16px;background:#8c8c8c}

/* footer */
.footer{position:absolute;left:0;top:988px;width:849px;height:212px;background:linear-gradient(180deg,#2b2b2b,var(--footer) 40%)}
.email{position:absolute;left:72px;top:52px;color:var(--white);font-size:18px}
.address{position:absolute;left:72px;top:92px;color:var(--orange);font-size:18px;line-height:25px;font-style:normal}
.brand{position:absolute;right:54px;top:28px;color:var(--orange);font-size:104px;font-weight:900;line-height:1}
.web{position:absolute;right:54px;top:150px;color:var(--white);font-size:18px}
</style>
</head>
<body>
<div class="flyer">
  <header class="header">
    <div class="header-photo" role="img" aria-label="Foto einer Tastatur mit oranger Taste HILFE"></div>
    <h1 class="headline">PC PROBLEME ???</h1>
    <p class="question">Wünschen Sie Sich manchmal eine<br>Hilfetaste die Ihnen Sofort Hilft ?</p>
    <p class="answer">..kein Problem, wir übernehmen dies<br>für Sie und helfen Ihnen Sofort !</p>
  </header>
  <div class="divider-dark"></div>

  <section class="main">
    <div class="hand-photo" role="img" aria-label="Foto einer einladend ausgestreckten Hand"></div>
    <div class="laptop-photo" role="img" aria-label="Foto eines aufgeklappten Laptops"></div>
    <div class="pc-photo" role="img" aria-label="Foto eines Desktop-PCs mit Tastatur und Maus"></div>

    <ul class="services">
      <li><span class="service-name">Reparaturen</span><span class="service-price">schon ab <b>59 €</b></span></li>
      <li><span class="service-name">Fernwartung</span><span class="service-price">schon ab <b>59 €</b></span></li>
      <li><span class="service-name">Neuinstallationen</span><span class="service-price">nur <b>49 €</b></span></li>
      <li><span class="service-name">Backups</span><span class="service-price">nur <b>59 €</b></span></li>
      <li><span class="service-name">Virenentfernung</span><span class="service-price">nur <b>69 €</b></span></li>
    </ul>

    <p class="pitch">Lassen Sie sich von unserem<br><em>Fachpersonal</em> <strong>Beraten</strong> und<br>von unseren <em>Profis</em> <strong>Helfen</strong></p>
    <p class="call">JETZT UNTER :<span class="phone">0800 / 4457718</span></p>
  </section>
  <div class="divider-light"></div>

  <footer class="footer">
    <p class="email">Email : info@pelmaro.net</p>
    <address class="address">Pelmaro GmbH<br>Musterstr.12<br>Musterhausen 33667</address>
    <p class="brand">pelmaro</p>
    <p class="web">www.pelmaro.de</p>
  </footer>
</div>
</body>
</html>
```